Brushline Cookout Product Labeling

We need a label design for a new product we are launching. We have developed a cooking bag that will cook your fish or game bird instantly. This is for the everyday fisherman and upland game hunter. This label will be printed on a thin sticker on the front of a Velnex Bag. The Velnex Bag is 9 1/2 x 12 inches. Inside the Velnex Bag is 3 cooking bags.
Target Market(s)
hunters and fishermen
Industry/Entity Type
Cooking
Font styles to use
Sans Serif
Colors
Designer to choose colors to be used in the design.
Requirements
Must have
- It must have "Brushline Cookout" logo. It should have Reed and Ridge. Reed and Ridge is the type of seasoning. It must have a small place on the label for net weight. It must also have the wording "Contains: 3 Individual Cooking Bags Inside.
Nice to have
- I really like a topographical map in the background. I have attached several images with products like that. It could also be cool having the background of the bag with a tiger trout's scales. I attached some images of that too. Some other ideas I thought i have is having a picture of the bird and fish on the bag. There is an GIF attached that has a cool looking fish that did that. There is also an image of a Brovik product that did the same thing.

```html
<!DOCTYPE html>
<html lang="en">
<head>
<meta charset="utf-8">
<title>Brushline Cookout – Reed and Ridge Label</title>
<link rel="stylesheet" href="https://fonts.googleapis.com/css2?family=Bebas+Neue&family=Oswald:wght@500;600&family=Roboto+Condensed:wght@600&display=swap">
<style>
  :root {
    --page-bg: #ededed;
    --label-bg: #ffffff;
    --topo-light: #f6f6f6;
    --topo-mid: #e9e9e9;
    --brand-red: #c7404a;
    --ink: #141414;
    --logo-panel: #0d0d0d;
    --logo-text: #ffffff;
  }
  * { margin: 0; padding: 0; box-sizing: border-box; }
  html, body {
    width: 1157px;
    height: 1200px;
    overflow: hidden;
    background: var(--page-bg);
  }
  .label {
    position: absolute;
    left: 143px;
    top: 50px;
    width: 871px;
    height: 1100px;
    background: var(--label-bg);
    border-radius: 8px;
    overflow: hidden;
  }
  .topo-background {
    position: absolute;
    inset: 0;
    background:
      radial-gradient(ellipse at 30% 25%, var(--topo-mid) 0%, transparent 45%),
      radial-gradient(ellipse at 75% 70%, var(--topo-mid) 0%, transparent 40%),
      var(--topo-light);
  }
  .logo-panel {
    position: absolute;
    left: 464px;
    top: 0;
    width: 357px;
    height: 243px;
    background: var(--logo-panel);
    border-radius: 0 0 10px 10px;
    display: flex;
    align-items: center;
    justify-content: center;
  }
  .logo-name {
    font-family: "Oswald", sans-serif;
    font-weight: 500;
    font-size: 34px;
    color: var(--logo-text);
    letter-spacing: 0.5px;
    text-transform: uppercase;
  }
  .product-title {
    position: absolute;
    left: 196px;
    top: 40px;
    height: 1020px;
    width: 224px;
    writing-mode: vertical-rl;
    transform: rotate(180deg);
    display: flex;
    align-items: center;
    justify-content: flex-start;
    font-family: "Bebas Neue", sans-serif;
    font-size: 228px;
    line-height: 1;
    color: var(--brand-red);
    white-space: nowrap;
  }
  .product-title .title-join {
    font-family: "Oswald", sans-serif;
    font-weight: 600;
    font-size: 64px;
    color: var(--ink);
    text-transform: lowercase;
    margin: 0 14px;
  }
  .game-art {
    position: absolute;
    left: 464px;
    top: 571px;
    width: 357px;
    height: 158px;
    background: linear-gradient(90deg, #d8d8d8, #c4c4c4);
    border-radius: 6px;
  }
  .info {
    position: absolute;
    left: 464px;
    top: 742px;
    width: 357px;
    color: var(--ink);
  }
  .audience {
    font-family: "Oswald", sans-serif;
    font-weight: 500;
    font-size: 29px;
    line-height: 46px;
    text-transform: uppercase;
    white-space: nowrap;
  }
  .rule {
    border: none;
    border-top: 3px solid var(--ink);
    margin: 18px 0 20px;
  }
  .contents {
    font-family: "Roboto Condensed", sans-serif;
    font-weight: 600;
    font-size: 28px;
    line-height: 47px;
    letter-spacing: 3px;
    text-transform: uppercase;
    white-space: nowrap;
  }
  .net-weight {
    font-family: "Oswald", sans-serif;
    font-weight: 500;
    font-size: 32px;
    text-align: center;
    text-transform: uppercase;
    margin-top: 22px;
  }
</style>
</head>
<body>
  <main class="label">
    <div class="topo-background" role="img" aria-label="Faint grey topographic contour map pattern"></div>

    <div class="logo-panel">
      <span class="logo-name">Brushline Cookout</span>
    </div>

    <h1 class="product-title">Reed<span class="title-join">and</span>Ridge</h1>

    <div class="game-art" role="img" aria-label="Black ink illustration of a pheasant and a trout"></div>

    <section class="info">
      <p class="audience">For the everyday fisherman<br>and upland game hunter</p>
      <hr class="rule">
      <p class="contents">Contains: 3 individual<br>cooking bags inside</p>
      <hr class="rule">
      <p class="net-weight">Net weight</p>
    </section>
  </main>
</body>
</html>
```